Recruitment process infographic

We are a boutique recruitment firm and we work remotely, connecting our candidates (mostly non-Japanese engineers) to exciting companies in Japan.
We have multiple steps in the process from scouting candidates on Linkfolio, reviewing their CV, helping them prepare for their interview etc. As there are multiple reps involved in each step of the progress, we'd like to prepare an infographic to help our candidates understand the flow of our process, answer their FAQs as well as sharing "who is who".
It should be a clean and clear representation of the candidate journey with our company, to make them feel comfortable knowing they are in safe hands. We welcome any recommendation in wording/format changes to make the process easier / cleaner to understand.
The end product should be on a platform where I can easily add/edit wording, as we need to keep our employee names updated whenever we hire someone new, or something in our process changes.
Here is the wording required. Company name and employee names have not been included at this stage.
https://pages.tarnwell-notes.com/sheet/d/8vLmQwe2Rt5YbnaHo3JkPzXc7dFgUs9Vb4HkLq-TnWx/edit
The infographic is required for the first page of the document, however we will need a second page (or more) for the FAQs so would be great to see a design that can accommodate that.
Branding/design guidelines:
A minimalistic, clean and clear look
Contrast with the logo (logo is orange on white background)
Icons / images will be great, just as long as they don't clutter the graphic
Process should build trust and inspire confidence
Meant to attracts followers/subscribers
Allows us to smoothly introduce our services/platforms
Typeface: Arial if possible, but open for other clean alternatives
Colours: see attachment
Engineers looking for jobs
Recruitment, IT

```html
<!DOCTYPE html>
<html lang="en">
<head>
<meta charset="utf-8">
<title>Frequently Asked Questions</title>
<link rel="stylesheet" href="https://fonts.googleapis.com/css2?family=Poppins:wght@500;600;700&family=Roboto:wght@400&display=swap">
<style>
  :root {
    --navy: #0a0d3a;
    --navy-text: #1c2053;
    --orange: #d2460e;
    --paper: #ececee;
    --strip: #f3f3f4;
    --stage: #cfcfd1;
    --ink: #16171c;
    --on-navy: #e9e9ef;
    --violet: #5a4fae;
  }
  * { box-sizing: border-box; margin: 0; padding: 0; }
  html, body { width: 1200px; height: 1068px; overflow: hidden; }
  body { background: var(--stage); position: relative; font-family: "Roboto", Arial, sans-serif; }

  .faq-sheet {
    position: absolute; left: 0; top: 112px;
    width: 1200px; height: 843px;
    background: var(--paper);
    overflow: hidden;
  }
  .edge-strip { position: absolute; left: 0; top: 0; width: 21px; height: 100%; background: var(--strip); }
  .company-panel {
    position: absolute; left: 21px; top: 0; width: 476px; height: 100%;
    background: var(--navy); color: var(--on-navy);
  }
  .title-tab { position: absolute; left: 0; top: 26px; width: 40px; height: 126px; background: var(--orange); }
  .sheet-title {
    position: absolute; left: 49px; top: 40px;
    font-family: "Poppins", Arial, sans-serif; font-weight: 700;
    font-size: 43px; line-height: 49px; color: #f1f1f5;
  }
  .section-heading {
    font-family: "Poppins", Arial, sans-serif; font-weight: 600;
    font-size: 23px; letter-spacing: -0.2px;
  }
  .company-panel .section-heading { position: absolute; left: 25px; top: 206px; color: #f1f1f5; }
  .company-faq { position: absolute; left: 25px; top: 255px; width: 425px; }

  .faq-item { margin-bottom: 15px; }
  .faq-question {
    font-family: "Poppins", Arial, sans-serif; font-weight: 600;
    font-size: 13.2px; line-height: 15.5px; margin-bottom: 2px;
  }
  .faq-answer { font-size: 11.2px; line-height: 13.6px; }
  .company-faq .faq-question { color: var(--orange); }
  .company-faq .faq-answer { color: var(--on-navy); }

  .process-panel { position: absolute; left: 497px; top: 0; width: 703px; height: 100%; }
  .process-rule { position: absolute; left: 0; bottom: 0; width: 703px; height: 6px; background: var(--orange); }
  .emergency { position: absolute; left: 24px; top: 50px; }
  .emergency-label {
    font-family: "Poppins", Arial, sans-serif; font-weight: 700;
    font-size: 17px; letter-spacing: 1.6px; color: var(--orange); margin-bottom: 4px;
  }
  .emergency-lines {
    font-family: "Poppins", Arial, sans-serif; font-weight: 500;
    font-size: 14px; line-height: 17px; color: var(--ink);
  }
  .question-art {
    position: absolute; left: 430px; top: 27px; width: 254px; height: 186px;
    background: radial-gradient(ellipse at 50% 45%, rgba(90,79,174,.55), rgba(90,79,174,.12) 55%, rgba(236,236,238,0) 75%);
    border-radius: 12px;
  }
  .process-panel .section-heading { position: absolute; left: 24px; top: 206px; color: var(--orange); }
  .process-faq { position: absolute; left: 24px; top: 255px; width: 640px; }
  .process-faq .faq-item { margin-bottom: 12px; }
  .process-faq .faq-question { color: var(--navy-text); }
  .process-faq .faq-answer { color: var(--ink); }
  .process-faq .faq-answer p + p { margin-top: 13px; }
</style>
</head>
<body>
  <section class="faq-sheet">
    <div class="edge-strip"></div>

    <div class="company-panel">
      <div class="title-tab"></div>
      <h1 class="sheet-title">Frequently<br>Asked Questions</h1>
      <h2 class="section-heading">ABOUT THE COMPANY</h2>
      <div class="company-faq">
        <div class="faq-item">
          <h3 class="faq-question">Q. Do you charge any fee? What is your<br>business model?</h3>
          <p class="faq-answer">A. We don’t charge any fee to our candidates!<br>Our clients (the companies) pay us a percentage if they decide to hire you. As part of our commitment to help Japanese companies thrive and become more diverse and inclusive, we also offer HR consulting services to them.</p>
        </div>
        <div class="faq-item">
          <h3 class="faq-question">Q. What is the benefit of using your service?</h3>
          <p class="faq-answer">A. We know that job hunting in general, especially in Japan, can be pretty tedious! When you register with us, you get access to jobs with some of Japan’s most exciting, forward-thinking companies that are keen to hire non-Japanese employees. We have a lot of job positions that don’t require Japanese and/or are fully remote. We take our motto “motto” seriously and commit to only work with companies that share our values, that treat employees with respect and do not discriminate.</p>
        </div>
        <div class="faq-item">
          <h3 class="faq-question">Q. Is there a phone number I can call you at?</h3>
          <p class="faq-answer">A. We mostly communicate via messages (quicker!).<br>The majority of our staff live around the world so we use Callspace calls or Meetloop. For emergencies before, during or after client interviews, we will provide you with a number to call.</p>
        </div>
        <div class="faq-item">
          <h3 class="faq-question">Q. Why are there so many people involved instead of just one recruiter?</h3>
          <p class="faq-answer">A. We are not your typical recruitment agency where numbers and individual sales are everything. You will have an expert in the field for each step of the process, timely support and a whole team looking after you!</p>
        </div>
        <div class="faq-item">
          <h3 class="faq-question">Q. Where is your office? I want to have a face to face meeting / Where are you based?</h3>
          <p class="faq-answer">A. Welcome to the new normal! Our business is now completely remote with most of our members not living in Tokyo anymore (OUR CEO*link to blog* is in xx!). With Covid-19 restrictions, we are also avoiding any physical interactions<br>to protect our staff. TGFMeetloop!</p>
        </div>
        <div class="faq-item">
          <h3 class="faq-question">Q. Do you work with overseas companies?</h3>
          <p class="faq-answer">A. We only work with companies that are hiring in Japan.</p>
        </div>
      </div>
    </div>

    <div class="process-panel">
      <div class="emergency">
        <div class="emergency-label">EMERGENCY CONTACT:</div>
        <div class="emergency-lines">hello@tarnwell-talent.com Or<br>Contact Any Of Us On Linkfolio!</div>
      </div>
      <div class="question-art" role="img" aria-label="Illustration of two people standing beside a large violet question mark"></div>
      <h2 class="section-heading">ABOUT THE PROCESS</h2>
      <div class="process-faq">
        <div class="faq-item">
          <h3 class="faq-question">Q. Can I just apply directly to the companies? Any difference between me directly applying and you recommending to the companies?</h3>
          <p class="faq-answer">A. While you can apply directly, most of our clients prefer to receive applications through us as we tailor our recommendations and prepare our candidates for interviews. Some clients receive so many applicants and tend to miss individual applications or applications from big agencies (as those are sent in bulk), but would always review ours, so you have a higher chance of getting an interview. It also saves you time and efforts as we can send your profile to all the companies you would be a suitable match for, on your behalf!</p>
        </div>
        <div class="faq-item">
          <h3 class="faq-question">Q. Where can I see my application/s status?</h3>
          <p class="faq-answer">A. If you log into the “My page” in our Bridgeway Careers website, you will be able to see all your ongoing applications status.</p>
        </div>
        <div class="faq-item">
          <h3 class="faq-question">Q. Is there any action required from my end? Do I need to go and apply for jobs?</h3>
          <div class="faq-answer">
            <p>A. Once you register on our website and have an introductory call with us, your profile will be on our database and we will continuously show you jobs that match you. There is no action required but just to keep an eye on your Linkfolio messages or your email. You also have the option to let us apply on your behalf for all the jobs that match your profile directly - this increases your chances to get an interview, as recruiting is all about timing!<br>You can also keep an eye on our website for new jobs and let us know if there’s any that interest you and you would like us to apply for.</p>
            <p>The only action required would be to keep us informed should your situation change (ex. you found a job, got a new qualification, moved to another region or country).</p>
          </div>
        </div>
        <div class="faq-item">
          <h3 class="faq-question">Q. I’m not in Japan, can I still get a job through you?</h3>
          <p class="faq-answer">A. We can only introduce jobs to candidates that hold a valid working visa in Japan. If you went back to your country temporarily but can still work in Japan, that is fine.</p>
        </div>
        <div class="faq-item">
          <h3 class="faq-question">Q. How long will the process take?</h3>
          <p class="faq-answer">A. Once you have registered on our website and spoken to one of our interviewers, we will start recommending your profile right away. Usually candidates start getting interview requests after about a week, however timing will depend on the companies and the availability of jobs for your role.</p>
        </div>
        <div class="faq-item">
          <h3 class="faq-question">Q. Can you tell me the name of the companies?</h3>
          <p class="faq-answer">A. Due to privacy regulations, we will only be able to disclose company names once you sign up on our website and speak to one of our interviewers.</p>
        </div>
        <div class="faq-item">
          <h3 class="faq-question">Q. If the companies ask me about my salary expectation, what should I do?</h3>
          <p class="faq-answer">A: While this shouldn’t happen, please do not talk about salary matters directly with the companies. We will be communicating and negotiating with the company on behalf of you.</p>
        </div>
      </div>
      <div class="process-rule"></div>
    </div>
  </section>
</body>
</html>
```